Wren Vehicle Polishing (Mobile detail)

I need a business card made up. I'd like it to be different in some form, either raised, embossed, debossed, something cool that stands out. (preferably embossed text somewhere in it). I will be including the Initial png file. Let me know if you need the photoshop of adobe illustrator file to work with.

Information to be included: Text: XXX-XXX-XXXX Phone: XXX-XXX-XXXX Email: wrenpolishcrew@mailbox-demo.net Website: www.socialpage-demo.net/wrenpolishKTR Hours of operation: Mon - Fri 7:00AM to 8:00PM Sat - 10:00AM to 8:00PM

Target Market(s)

Mobile automotive detailing

Industry/Entity Type

Automotive

Contact Information for Business Card

Make it stand out with embossed lettering, I'd also like the background to be glossy black or matte, something that represents a shiny car, black preferred

Requirements
Must have
• A glossy background, or something.
• My logo, pick one of them that best fits your design.
Should not have
• White background,
• something that does not stand out.

```html
<!DOCTYPE html>
<html lang="en">
<head>
<meta charset="utf-8">
<title>Wren Vehicle Polishing – Business Card</title>
<link href="https://fonts.googleapis.com/css2?family=Roboto:wght@400;500;700&display=swap" rel="stylesheet">
<style>
  :root {
    --page: #d8d4ce;
    --card-black: #111213;
    --card-mid: #1c1d1f;
    --sheen: rgba(255,255,255,0.10);
    --orange: #f0581e;
    --orange-light: #ff8a2a;
    --white: #f2f2f2;
    --grey: #b9bcc0;
    --grey-dark: #7c8086;
  }
  * { box-sizing: border-box; margin: 0; padding: 0; }
  html, body {
    width: 1200px; height: 950px; overflow: hidden;
    background: var(--page);
    font-family: "Roboto", Arial, sans-serif;
  }
  .sheet {
    width: 1200px; height: 950px;
    display: flex; flex-direction: column; align-items: center; justify-content: center;
    gap: 28px;
  }
  .card {
    position: relative;
    width: 760px; height: 434px;
    border-radius: 6px;
    overflow: hidden;
    background:
      linear-gradient(115deg, transparent 0 52%, var(--sheen) 58%, transparent 70%),
      radial-gradient(ellipse at 60% 30%, var(--card-mid), var(--card-black) 75%);
    box-shadow: 0 14px 30px rgba(0,0,0,0.35);
    color: var(--white);
  }

  /* Brand name lockup (stands in for the logo mark) */
  .brand {
    position: absolute;
    display: flex; align-items: center; gap: 14px;
  }
  .brand-dot {
    width: 30px; height: 30px; border-radius: 50%;
    background: var(--orange);
    flex: none;
  }
  .brand-name {
    font-weight: 700;
    font-size: 30px;
    line-height: 1.1;
    color: var(--grey);
    letter-spacing: 0.5px;
  }

  /* Back side */
  .card-back .brand { left: 50%; top: 120px; transform: translateX(-50%); }
  .hours {
    position: absolute; left: 0; right: 0; top: 268px;
    text-align: center;
  }
  .hours-title {
    font-weight: 700; font-size: 22px; color: var(--orange);
    letter-spacing: 1px;
  }
  .hours-times {
    margin-top: 10px; font-size: 19px; color: var(--grey);
  }
  .hours-times .divider { color: var(--orange); margin: 0 10px; }

  /* Front side */
  .person { position: absolute; left: 56px; top: 110px; }
  .person-name { font-size: 28px; font-weight: 500; color: var(--orange); letter-spacing: 0.5px; }
  .person-role { font-size: 19px; color: var(--white); margin-top: 4px; letter-spacing: 0.5px; }
  .phones { position: absolute; left: 56px; top: 196px; list-style: none; }
  .phones li { display: flex; align-items: center; gap: 12px; font-size: 21px; margin-bottom: 6px; }
  .phones svg { width: 18px; height: 18px; flex: none; }

  .rule-top {
    position: absolute; left: 0; top: 272px; width: 480px; height: 1.5px;
    background: var(--orange);
  }
  .rule-bottom {
    position: absolute; right: 36px; top: 362px; width: 320px; height: 1.5px;
    background: var(--orange);
  }
  .card-front .brand { left: 440px; top: 150px; width: 260px; }

  .contact { position: absolute; right: 36px; top: 298px; list-style: none; text-align: right; }
  .contact li { display: flex; align-items: center; justify-content: flex-end; gap: 10px; font-size: 18px; margin-bottom: 8px; color: var(--white); }
  .contact svg { width: 16px; height: 14px; flex: none; }

  .band {
    position: absolute; left: 0; right: 0; bottom: 0; height: 20px; display: flex;
  }
  .band-orange { width: 56%; background: linear-gradient(90deg, var(--orange-light), var(--orange)); }
  .band-grey { flex: 1; background: linear-gradient(90deg, var(--grey), var(--grey-dark)); }
</style>
</head>
<body>
<main class="sheet">

  <section class="card card-back" aria-label="Card back">
    <div class="brand">
      <span class="brand-dot"></span>
      <span class="brand-name">Wren Vehicle Polishing</span>
    </div>
    <div class="hours">
      <p class="hours-title">HOURS OF OPERATION</p>
      <p class="hours-times">Mon - Fri 7:00AM to 8:00PM<span class="divider">|</span>Sat - 10:00AM to 8:00PM</p>
    </div>
  </section>

  <section class="card card-front" aria-label="Card front">
    <div class="person">
      <p class="person-name">DALE MARSH</p>
      <p class="person-role">DETAILER</p>
    </div>
    <ul class="phones">
      <li>
        <svg viewBox="0 0 18 18" aria-hidden="true"><rect x="4.5" y="1" width="9" height="16" rx="1.5" fill="none" stroke="#f0581e" stroke-width="1.6"/><circle cx="9" cy="14.3" r="0.9" fill="#f0581e"/></svg>
        555-014-2290
      </li>
      <li>
        <svg viewBox="0 0 18 18" aria-hidden="true"><path d="M2 7 Q9 1 16 7 L14 9 L12 7.5 L12 6 Q9 5 6 6 L6 7.5 L4 9 Z" fill="#f0581e"/><rect x="4" y="10" width="10" height="6" rx="1" fill="#f0581e"/></svg>
        555-019-7731
      </li>
    </ul>
    <div class="rule-top"></div>

    <div class="brand">
      <span class="brand-dot"></span>
      <span class="brand-name">Wren Vehicle Polishing</span>
    </div>

    <ul class="contact">
      <li>wrenpolishcrew@mailbox-demo.net
        <svg viewBox="0 0 16 14" aria-hidden="true"><rect x="0.5" y="1" width="15" height="12" rx="1" fill="#f0581e"/><path d="M1 2 L8 8 L15 2" fill="none" stroke="#111213" stroke-width="1.3"/></svg>
      </li>
      <li>socialpage-demo.net/wrenpolishKTR
        <svg viewBox="0 0 16 14" aria-hidden="true"><rect x="1" y="0" width="14" height="14" rx="2" fill="#f0581e"/></svg>
      </li>
    </ul>
    <div class="rule-bottom"></div>

    <div class="band">
      <div class="band-orange"></div>
      <div class="band-grey"></div>
    </div>
  </section>

</main>
</body>
</html>
```